Marketing Flyer for Plumber Referals

8.5" x11" Layout should be landscape not portrait. Create a bold, eye-catching flyer that highlights earning potential from referrals for water damage restoration. Use high-contrast colors like blue, yellow, and white, with bold fonts and dynamic layouts. Include images of restoration work, cash, and happy clients. Emphasize key benefits like $500 minimum payouts, fast payments, and unlimited income potential. Keep instructions simple: refer a client, we handle the work, you get paid. Add a clear call-to-action and display contact details prominently. Focus on professionalism and energy.

Target Market(s)

Plumbers and Contractor 8.5" x11" Layout should be landscape not portrait.

Industry/Entity Type

General Contractor

Colors
0054AA
0677BA
7BADD7
CADEEF
E8F1F8
EB3D1F
EC4F4E
F09395
F8D3D4
FCEDEE

Requirements
Must have
• 8.5" x11" Layout should be landscape not portrait.
Nice to have

```html
<!DOCTYPE html>
<html lang="en">
<head>
<meta charset="utf-8">
<title>Bayline Remodel – Referral Flyer</title>
<link href="https://fonts.googleapis.com/css2?family=Hind:wght@400;500;600;700&display=swap" rel="stylesheet">
<style>
:root{
  --backdrop:#d3d7dc;
  --paper:#ffffff;
  --ink:#14213a;
  --blue-deep:#0054AA;
  --blue:#0677BA;
  --blue-mid:#7BADD7;
  --blue-soft:#CADEEF;
  --blue-mist:#E8F1F8;
  --red:#EB3D1F;
  --red-soft:#EC4F4E;
  --red-pale:#FCEDEE;
  --white:#ffffff;
}
*{margin:0;padding:0;box-sizing:border-box}
html,body{width:1200px;height:2254px;overflow:hidden;background:var(--backdrop);font-family:"Hind",sans-serif;color:var(--ink)}
.page{position:absolute;left:50px;width:1100px;height:850px;background:var(--paper);overflow:hidden}
.page--front{top:160px}
.page--back{top:1244px}
.abs{position:absolute}

/* front */
.headline{left:50px;top:62px;font-size:32px;font-weight:700;line-height:38px;letter-spacing:.5px;text-transform:uppercase;color:var(--blue-deep)}
.offer{left:50px;top:168px;width:540px;height:132px;border:2px solid var(--red);border-radius:16px;background:var(--red-pale)}
.offer-main{position:absolute;left:30px;top:24px;font-weight:700;white-space:nowrap;color:var(--ink)}
.offer-amount{font-size:48px;color:var(--red)}
.offer-rest{font-size:23px;margin-left:10px}
.offer-sub{position:absolute;left:30px;top:86px;font-size:17px;font-weight:500}

.band{left:0;top:334px;width:590px;height:58px;background:var(--blue-deep);color:var(--white);font-size:34px;font-weight:700;line-height:64px;padding-left:50px;letter-spacing:.5px}

.benefits{left:50px;top:420px;width:560px;list-style:none;font-size:16px;line-height:25px}
.benefits li{margin-bottom:8px;padding-left:16px;position:relative}
.benefits li::before{content:"";position:absolute;left:0;top:9px;width:7px;height:7px;background:var(--red)}
.benefits strong{font-weight:600;color:var(--blue-deep)}

.tagline{left:50px;top:640px;font-size:25px;font-weight:700;color:var(--red)}
.accent-bar{left:0;top:820px;width:640px;height:30px;background:var(--blue-deep)}
.accent-bar-tip{left:0;top:808px;width:640px;height:12px;background:var(--blue-soft)}

.photo-skyline{left:640px;top:0;width:460px;height:850px;background:linear-gradient(180deg,#7BADD7 0%,#CADEEF 38%,#0677BA 58%,#0054AA 74%,#0b3a70 100%)}
.brand-box{left:900px;top:40px;width:160px;height:110px;background:var(--white);display:flex;align-items:center;justify-content:center;text-align:center}
.brand-name{color:var(--blue-deep);font-size:19px;font-weight:700;letter-spacing:1px;line-height:22px;text-transform:uppercase}

/* back */
.photo-flood{left:0;top:0;width:600px;height:770px;background:linear-gradient(180deg,#E8F1F8 0%,#CADEEF 35%,#7BADD7 60%,#0677BA 82%,#0054AA 100%)}
.hero-panel{left:0;top:460px;width:620px;height:250px;background:var(--red)}
.hero-title{position:absolute;left:50px;top:50px;color:var(--white);font-size:60px;font-weight:700;line-height:72px;letter-spacing:1px;text-transform:uppercase}

.steps-title{left:660px;top:86px;font-size:38px;font-weight:700;letter-spacing:.5px;text-transform:uppercase;color:var(--blue-deep)}
.steps-rule{left:660px;top:142px;width:80px;height:5px;background:var(--red)}
.steps{left:660px;top:176px;width:400px;list-style:none;font-size:19px;line-height:28px}
.step{margin-bottom:26px}
.step-name{font-weight:700;color:var(--blue-deep)}
.step-detail{padding-left:22px;position:relative;margin-top:4px}
.step-detail::before{content:"";position:absolute;left:2px;top:9px;width:9px;height:9px;border:2px solid var(--red);border-radius:50%}

.footer{left:0;top:770px;width:1100px;height:80px;background:var(--blue-deep);color:var(--white);text-align:center;font-size:20px;line-height:26px;padding-top:15px}
.footer-contact{font-weight:700}
</style>
</head>
<body>

<section class="page page--front">
  <h1 class="abs headline">Earn Unlimited Cash<br>Get Paid to Refer a Flood</h1>

  <div class="abs offer">
    <p class="offer-main"><span class="offer-amount">$500</span><span class="offer-rest">Minimum or 10% Per Referral!</span></p>
    <p class="offer-sub">Partner with the #1 Water Damage Restoration Team</p>
  </div>

  <h2 class="abs band">WHY PARTNER WITH US?</h2>
  <ul class="abs benefits">
    <li><strong>Guaranteed Payout:</strong> Minimum $500 or 10% of the invoice, paid fast.</li>
    <li><strong>Free Evaluations:</strong> We assess damage and process insurance claims for your clients.</li>
    <li><strong>Industry Leaders:</strong> Certified experts with 24/7 rapid response.</li>
    <li><strong>Affordable Solutions:</strong> Lowest out-of-pocket costs for your customers.</li>
  </ul>
  <p class="abs tagline">Send Referrals. Get Paid. Grow Your Business.</p>
  <div class="abs accent-bar-tip"></div>
  <div class="abs accent-bar"></div>

  <div class="abs photo-skyline" role="img" aria-label="City skyline at dusk reflected over a bay"></div>
  <div class="abs brand-box"><span class="brand-name">Bayline<br>Remodel</span></div>
</section>

<section class="page page--back">
  <div class="abs photo-flood" role="img" aria-label="Flooded home interior with water covering the floor at the foot of a staircase"></div>
  <div class="abs hero-panel">
    <h2 class="hero-title">Get Paid to<br>Refer a Flood</h2>
  </div>

  <h2 class="abs steps-title">How It Works</h2>
  <div class="abs steps-rule"></div>
  <ol class="abs steps">
    <li class="step">
      <p class="step-name">1. Refer Flood, Water and Mold Damage</p>
      <p class="step-detail">Call, book online, or text us directly.</p>
    </li>
    <li class="step">
      <p class="step-name">2. We Take Care of Everything</p>
      <p class="step-detail">Free evaluations, insurance claims, and professional service.</p>
    </li>
    <li class="step">
      <p class="step-name">3. Get Paid Fast</p>
      <p class="step-detail">$500 minimum or 10% of the invoice within 48 hours of final payment.</p>
    </li>
  </ol>

  <footer class="abs footer">
    Call Text or Book On-line<br>
    <span class="footer-contact">555-014-2290 | BaylineRemodel.com</span>
  </footer>
</section>

</body>
</html>
```